Kestrel Ink BC 2019

Hi!
As seen from the attached, I created a 2018 BC that I really like.
It features company details on one side, and a calendar on the other side. The BC is 7" x 2" with a score, so folded it's a regular sized BC.
Company details remain the same, but I need to upgrade and refresh the calendar to 2019. Let your creative juices flow!

The submitted designs so far, while not terrible, most don't take into account that I need a refresher on the current design, but it's a BC that is double sided, and the size of a BC that's side by side wide, with score. (see the attached BC 2018 design). I need the BC to be updated with a 2019 calendar, but essentially because it's such a tiny size, to work the realistic space allocated, and make it readable and striking to stand out and very usable/practical. Let's do this people!

```html
<!DOCTYPE html>
<html lang="en">
<head>
<meta charset="utf-8">
<title>Kestrel Ink – 2019 Calendar Card</title>
<link rel="stylesheet" href="https://fonts.googleapis.com/css2?family=Arimo:wght@400;700&display=swap">
<style>
  :root {
    --ink: #1d1d1b;
    --paper: #ffffff;
    --facet-light: #f4f4f4;
    --facet-mid: #e6e6e6;
    --weekend: #e3001b;
    --cyan: #1ea4dd;
    --magenta: #d6166f;
    --yellow: #e4d81c;
    --violet: #5b3d97;
    --orange: #f26a2c;
    --lime: #9ccc2e;
    --teal: #10a8a8;
    --rule: #333333;
  }
  * { box-sizing: border-box; margin: 0; padding: 0; }
  html, body { width: 1200px; height: 662px; overflow: hidden; }
  body { font-family: "Arimo", Arial, sans-serif; color: var(--ink); background: var(--paper); }

  .card {
    position: relative; width: 1200px; height: 662px; overflow: hidden;
    background: linear-gradient(135deg, var(--paper) 0%, var(--facet-light) 35%, var(--facet-mid) 55%, var(--facet-light) 75%, var(--paper) 100%);
  }

  /* brand */
  .brand-name {
    position: absolute; left: 176px; top: 176px;
    font-size: 40px; line-height: 40px; font-weight: 400; color: var(--ink);
    letter-spacing: 0.5px;
  }

  /* contact */
  .contact {
    position: absolute; right: 70px; top: 26px; text-align: right;
    font-size: 16px; line-height: 26px; color: var(--ink);
  }
  .contact-row { display: flex; justify-content: flex-end; align-items: center; gap: 18px; }
  .contact-item { display: inline-flex; align-items: center; gap: 6px; }
  .contact-item svg { width: 14px; height: 14px; }
  .divider-line { width: 28px; height: 2px; background: linear-gradient(90deg, var(--cyan), var(--magenta), var(--yellow)); }

  /* slogan */
  .slogan {
    position: absolute; left: 390px; top: 122px; width: 740px;
    font-size: 34px; font-weight: 400; padding-left: 0;
  }
  .slogan-rule { position: absolute; left: 386px; top: 170px; width: 744px; height: 1.5px; background: var(--rule); }
  .values {
    position: absolute; left: 386px; top: 181px; display: flex; gap: 8px;
    font-size: 18px; white-space: nowrap;
  }
  .value { display: inline-flex; align-items: center; gap: 3px; }
  .dot { width: 12px; height: 12px; border-radius: 50%; display: inline-block; }
  .dot-cyan { background: var(--cyan); }
  .dot-magenta { background: var(--magenta); }
  .dot-yellow { background: var(--yellow); }

  /* ornamental band */
  .band {
    position: absolute; left: 0; top: 292px; width: 1200px; height: 84px;
    background: linear-gradient(90deg,
      var(--violet) 0%, var(--magenta) 7%, var(--orange) 13%, var(--yellow) 17%, var(--teal) 24%,
      var(--violet) 30%, var(--magenta) 36%, var(--lime) 42%, var(--orange) 46%, var(--violet) 52%,
      var(--orange) 58%, var(--yellow) 62%, var(--lime) 68%, var(--teal) 74%, var(--magenta) 80%,
      var(--teal) 86%, var(--orange) 92%, var(--violet) 100%);
    clip-path: polygon(0 0, 100% 0, 100% 100%, 0 100%);
  }

  /* year block */
  .year { position: absolute; left: 63px; top: 438px; font-size: 50px; line-height: 56px; }
  .year-rule { position: absolute; left: 64px; top: 500px; width: 110px; height: 1px; background: var(--rule); }
  .motto { position: absolute; left: 62px; top: 506px; font-size: 30px; line-height: 23px; }
  .motto span { display: block; }
  .motto .cyan { color: var(--cyan); }
  .motto .magenta { color: var(--magenta); }
  .motto .yellow { color: var(--yellow); }

  /* calendar */
  .month { position: absolute; width: 138px; }
  .month h3 { text-align: center; font-size: 18px; font-weight: 400; line-height: 20px; margin-bottom: 1px; }
  .days { display: grid; grid-template-columns: repeat(7, 1fr); font-size: 9px; font-weight: 700; text-align: center; }
  .days > * { height: 15.5px; line-height: 15.5px; font-style: normal; }
  .days b { font-size: 12px; font-weight: 400; line-height: 17px; height: 19px; border-bottom: 1px solid var(--rule); margin-bottom: 1px; }
  .days > :nth-child(7n+6), .days > :nth-child(7n) { color: var(--weekend); }
  .days .pair { font-size: 7px; letter-spacing: -0.4px; }

  .row-top { top: 390px; }
  .row-bottom { top: 527px; }
  .c1 { left: 224px; } .c2 { left: 386px; } .c3 { left: 549px; }
  .c4 { left: 714px; } .c5 { left: 877px; } .c6 { left: 1040px; }
</style>
</head>
<body>
<main class="card">

  <div class="brand-name">Kestrel Ink</div>

  <div class="contact">
    <div class="contact-row">
      <span class="contact-item">
        <svg viewBox="0 0 16 16"><path d="M4 1l3 3-2 2c1 2 3 4 5 5l2-2 3 3-2 3C7 15 1 9 1 3z" fill="var(--ink)"/></svg>555.010.2233
      </span>
      <span class="contact-item">
        <svg viewBox="0 0 16 16"><rect x="1" y="3" width="11" height="8" rx="1.5" fill="var(--ink)"/><path d="M4 11v3l3-3z" fill="var(--ink)"/></svg>555.010.4477
      </span>
      <span class="contact-item">
        <svg viewBox="0 0 16 16"><rect x="1" y="4" width="14" height="10" rx="1" fill="none" stroke="var(--ink)" stroke-width="1.6"/><rect x="4" y="1" width="8" height="5" fill="var(--ink)"/></svg>555.010.2234
      </span>
    </div>
    <div class="contact-row">
      <span class="contact-item">
        <svg viewBox="0 0 16 16"><rect x="1" y="3" width="14" height="10" rx="1" fill="none" stroke="var(--ink)" stroke-width="1.6"/><path d="M1 4l7 5 7-5" fill="none" stroke="var(--ink)" stroke-width="1.6"/></svg>pickup@kestrelink.com
      </span>
      <span class="divider-line"></span>
      <span class="contact-item">
        <svg viewBox="0 0 16 16"><circle cx="8" cy="8" r="6.5" fill="none" stroke="var(--ink)" stroke-width="1.4"/><ellipse cx="8" cy="8" rx="3" ry="6.5" fill="none" stroke="var(--ink)" stroke-width="1.2"/><path d="M1.5 8h13" stroke="var(--ink)" stroke-width="1.2"/></svg>kestrelink.com
      </span>
    </div>
  </div>

  <h1 class="slogan">We do good stuff with your stuff !</h1>
  <div class="slogan-rule"></div>
  <p class="values">
    <span class="value"><i class="dot dot-cyan"></i>Fill your toner with purpose</span>
    <span class="value"><i class="dot dot-magenta"></i>Fill your planet with hope</span>
    <span class="value"><i class="dot dot-yellow"></i>Fill your world with kidness</span>
  </p>

  <div class="band" role="img" aria-label="Band of overlapping coloured geometric facets in violet, magenta, orange, yellow, lime and teal"></div>

  <div class="year">2019</div>
  <div class="year-rule"></div>
  <p class="motto"><span class="cyan">Fill your</span><span class="magenta">day with</span><span class="yellow">purpose.</span></p>

  <section class="month row-top c1"><h3>January</h3><div class="days">
    <b>M</b><b>T</b><b>W</b><b>T</b><b>F</b><b>S</b><b>S</b>
    <i></i><span>1</span><span>2</span><span>3</span><span>4</span><span>5</span><span>6</span>
    <span>7</span><span>8</span><span>9</span><span>10</span><span>11</span><span>12</span><span>13</span>
    <span>14</span><span>15</span><span>16</span><span>17</span><span>18</span><span>19</span><span>20</span>
    <span>21</span><span>22</span><span>23</span><span>24</span><span>25</span><span>26</span><span>27</span>
    <span>28</span><span>29</span><span>30</span><span>31</span>
  </div></section>

  <section class="month row-top c2"><h3>February</h3><div class="days">
    <b>M</b><b>T</b><b>W</b><b>T</b><b>F</b><b>S</b><b>S</b>
    <i></i><i></i><i></i><i></i><span>1</span><span>2</span><span>3</span>
    <span>4</span><span>5</span><span>6</span><span>7</span><span>8</span><span>9</span><span>10</span>
    <span>11</span><span>12</span><span>13</span><span>14</span><span>15</span><span>16</span><span>17</span>
    <span>18</span><span>19</span><span>20</span><span>21</span><span>22</span><span>23</span><span>24</span>
    <span>25</span><span>26</span><span>27</span><span>28</span>
  </div></section>

  <section class="month row-top c3"><h3>March</h3><div class="days">
    <b>M</b><b>T</b><b>W</b><b>T</b><b>F</b><b>S</b><b>S</b>
    <i></i><i></i><i></i><i></i><span>1</span><span>2</span><span>3</span>
    <span>4</span><span>5</span><span>6</span><span>7</span><span>8</span><span>9</span><span>10</span>
    <span>11</span><span>12</span><span>13</span><span>14</span><span>15</span><span>16</span><span>17</span>
    <span>18</span><span>19</span><span>20</span><span>21</span><span>22</span><span>23</span><span>24</span>
    <span>25</span><span>26</span><span>27</span><span>28</span><span>29</span><span>30</span><span>31</span>
  </div></section>

  <section class="month row-top c4"><h3>April</h3><div class="days">
    <b>M</b><b>T</b><b>W</b><b>T</b><b>F</b><b>S</b><b>S</b>
    <span>1</span><span>2</span><span>3</span><span>4</span><span>5</span><span>6</span><span>7</span>
    <span>8</span><span>9</span><span>10</span><span>11</span><span>12</span><span>13</span><span>14</span>
    <span>15</span><span>16</span><span>17</span><span>18</span><span>19</span><span>20</span><span>21</span>
    <span>22</span><span>23</span><span>24</span><span>25</span><span>26</span><span>27</span><span>28</span>
    <span>29</span><span>30</span>
  </div></section>

  <section class="month row-top c5"><h3>May</h3><div class="days">
    <b>M</b><b>T</b><b>W</b><b>T</b><b>F</b><b>S</b><b>S</b>
    <i></i><i></i><span>1</span><span>2</span><span>3</span><span>4</span><span>5</span>
    <span>6</span><span>7</span><span>8</span><span>9</span><span>10</span><span>11</span><span>12</span>
    <span>13</span><span>14</span><span>15</span><span>16</span><span>17</span><span>18</span><span>19</span>
    <span>20</span><span>21</span><span>22</span><span>23</span><span>24</span><span>25</span><span>26</span>
    <span>27</span><span>28</span><span>29</span><span>30</span><span>31</span>
  </div></section>

  <section class="month row-top c6"><h3>June</h3><div class="days">
    <b>M</b><b>T</b><b>W</b><b>T</b><b>F</b><b>S</b><b>S</b>
    <i></i><i></i><i></i><i></i><i></i><span>1</span><span>2</span>
    <span>3</span><span>4</span><span>5</span><span>6</span><span>7</span><span>8</span><span>9</span>
    <span>10</span><span>11</span><span>12</span><span>13</span><span>14</span><span>15</span><span>16</span>
    <span>17</span><span>18</span><span>19</span><span>20</span><span>21</span><span>22</span><span>23</span>
    <span>24</span><span>25</span><span>26</span><span>27</span><span>28</span><span>29</span><span>30</span>
  </div></section>

  <section class="month row-bottom c1"><h3>July</h3><div class="days">
    <b>M</b><b>T</b><b>W</b><b>T</b><b>F</b><b>S</b><b>S</b>
    <span>1</span><span>2</span><span>3</span><span>4</span><span>5</span><span>6</span><span>7</span>
    <span>8</span><span>9</span><span>10</span><span>11</span><span>12</span><span>13</span><span>14</span>
    <span>15</span><span>16</span><span>17</span><span>18</span><span>19</span><span>20</span><span>21</span>
    <span>22</span><span>23</span><span>24</span><span>25</span><span>26</span><span>27</span><span>28</span>
    <span>29</span><span>30</span><span>31</span>
  </div></section>

  <section class="month row-bottom c2"><h3>August</h3><div class="days">
    <b>M</b><b>T</b><b>W</b><b>T</b><b>F</b><b>S</b><b>S</b>
    <i></i><i></i><i></i><span>1</span><span>2</span><span>3</span><span>4</span>
    <span>5</span><span>6</span><span>7</span><span>8</span><span>9</span><span>10</span><span>11</span>
    <span>12</span><span>13</span><span>14</span><span>15</span><span>16</span><span>17</span><span>18</span>
    <span>19</span><span>20</span><span>21</span><span>22</span><span>23</span><span>24</span><span>25</span>
    <span>26</span><span>27</span><span>28</span><span>29</span><span>30</span><span>31</span>
  </div></section>

  <section class="month row-bottom c3"><h3>September</h3><div class="days">
    <b>M</b><b>T</b><b>W</b><b>T</b><b>F</b><b>S</b><b>S</b>
    <i></i><i></i><i></i><i></i><i></i><i></i><span>1</span>
    <span>2</span><span>3</span><span>4</span><span>5</span><span>6</span><span>7</span><span>8</span>
    <span>9</span><span>10</span><span>11</span><span>12</span><span>13</span><span>14</span><span>15</span>
    <span>16</span><span>17</span><span>18</span><span>19</span><span>20</span><span>21</span><span>22</span>
    <span class="pair">23/30</span><span>24</span><span>25</span><span>26</span><span>27</span><span>28</span><span>29</span>
  </div></section>

  <section class="month row-bottom c4"><h3>October</h3><div class="days">
    <b>M</b><b>T</b><b>W</b><b>T</b><b>F</b><b>S</b><b>S</b>
    <i></i><span>1</span><span>2</span><span>3</span><span>4</span><span>5</span><span>6</span>
    <span>7</span><span>8</span><span>9</span><span>10</span><span>11</span><span>12</span><span>13</span>
    <span>14</span><span>15</span><span>16</span><span>17</span><span>18</span><span>19</span><span>20</span>
    <span>21</span><span>22</span><span>23</span><span>24</span><span>25</span><span>26</span><span>27</span>
    <span>28</span><span>29</span><span>30</span><span>31</span>
  </div></section>

  <section class="month row-bottom c5"><h3>November</h3><div class="days">
    <b>M</b><b>T</b><b>W</b><b>T</b><b>F</b><b>S</b><b>S</b>
    <i></i><i></i><i></i><i></i><span>1</span><span>2</span><span>3</span>
    <span>4</span><span>5</span><span>6</span><span>7</span><span>8</span><span>9</span><span>10</span>
    <span>11</span><span>12</span><span>13</span><span>14</span><span>15</span><span>16</span><span>17</span>
    <span>18</span><span>19</span><span>20</span><span>21</span><span>22</span><span>23</span><span>24</span>
    <span>25</span><span>26</span><span>27</span><span>28</span><span>29</span><span>30</span>
  </div></section>

  <section class="month row-bottom c6"><h3>December</h3><div class="days">
    <b>M</b><b>T</b><b>W</b><b>T</b><b>F</b><b>S</b><b>S</b>
    <i></i><i></i><i></i><i></i><i></i><i></i><span>1</span>
    <span>2</span><span>3</span><span>4</span><span>5</span><span>6</span><span>7</span><span>8</span>
    <span>9</span><span>10</span><span>11</span><span>12</span><span>13</span><span>14</span><span>15</span>
    <span>16</span><span>17</span><span>18</span><span>19</span><span>20</span><span>21</span><span>22</span>
    <span class="pair">23/30</span><span class="pair">24/31</span><span>25</span><span>26</span><span>27</span><span>28</span><span>29</span>
  </div></section>

</main>
</body>
</html>
```